Corbelle Group - Business Cards

We would need to design our Company Business Cards for the following People:

1. Martin Cole
Director/Licensee-In-Charge
M: 0417 524 903
T: (02) 7354 2260
E: martin@corbelle.com.au
Website: www.corbellegroup.com

2. Derek Holm
Project Manager
M: 0428 613 954
T: (02) 7354 2260
E: derek@corbellegroup.com

3. Priya Venkataraman
Property Officer
M: 0439 271 806
T: (02) 7354 2260
E: priya@corbellegroup.com

Address: Level 9, 42 Harlow Road W, Parramatta NSW 2150
The above address is the SAME for ALL Cards.

This Card is to be Double-Sided.
Front - With the above Information & Details.
Back - Showing the Services:
Property Services, Financial Solutions, Special Projects.

ALL Office Locations:
Sydney: (02) 7354 2260
Melbourne: (03) 9412 5063
Brisbane: (07) 3275 4190
Malaysia (JB): (+601) 8340 2967
Singapore: (+65) 9481 2736

We intend on making a Design/Template for the Business Card & duplicating these Business Cards for the above 3x People.
Please USE & REFER to the above FULL Name, Job Title, Mobile, Office Phone, Email & Website.

```html
<!DOCTYPE html>
<html lang="en">
<head>
<meta charset="utf-8">
<title>Corbelle Group – Business Cards</title>
<link href="https://fonts.googleapis.com/css2?family=Work+Sans:wght@400;500;600&display=swap" rel="stylesheet">
<style>
  :root {
    --bg: #1b1b1c;
    --card: #4f5052;
    --card-light: #5a5b5e;
    --yellow: #e3e11d;
    --white: #ffffff;
    --text: #f2f2f2;
  }
  * { margin: 0; padding: 0; box-sizing: border-box; }
  html, body { width: 1200px; height: 900px; overflow: hidden; }
  body {
    background: var(--bg);
    font-family: "Work Sans", Arial, sans-serif;
    color: var(--text);
    position: relative;
  }
  .card {
    position: absolute;
    left: 290px;
    width: 620px;
    height: 370px;
    background: linear-gradient(135deg, var(--card-light), var(--card));
    overflow: hidden;
  }
  .card-back { top: 60px; }
  .card-front { top: 470px; }

  .wordmark {
    position: absolute;
    display: flex;
    align-items: center;
    gap: 12px;
    font-weight: 500;
    color: var(--white);
    line-height: 1;
    white-space: nowrap;
  }
  .wordmark .mark-square {
    width: 0.6em;
    height: 0.6em;
    background: var(--yellow);
    flex: none;
  }
  .card-back .wordmark { left: 0; right: 0; justify-content: center; top: 110px; font-size: 34px; }
  .card-front .wordmark { right: 30px; top: 34px; font-size: 26px; }

  .offices {
    position: absolute;
    left: 0; right: 0; top: 200px;
    text-align: center;
    font-size: 14px;
    font-weight: 500;
    line-height: 1.45;
    letter-spacing: 0.04em;
  }
  .sep { color: var(--yellow); padding: 0 4px; }
  .services {
    position: absolute;
    left: 0; right: 0; top: 300px;
    text-align: center;
    font-size: 16px;
    font-weight: 500;
    letter-spacing: 0.05em;
  }

  .person { position: absolute; left: 40px; top: 80px; }
  .person-name {
    color: var(--yellow);
    font-size: 30px;
    font-weight: 500;
    letter-spacing: 0.02em;
    text-transform: uppercase;
    line-height: 1;
  }
  .person-title { font-size: 18px; margin-top: 6px; letter-spacing: 0.04em; }
  .divider {
    position: absolute;
    left: 30px; right: 30px; top: 145px;
    height: 2px;
    background: var(--yellow);
  }
  .contacts { position: absolute; left: 40px; top: 162px; list-style: none; }
  .contacts li {
    display: flex; align-items: center; gap: 10px;
    font-size: 18px; line-height: 28px; letter-spacing: 0.03em;
  }
  .contacts svg { width: 13px; height: 13px; flex: none; }
  .highlight { color: var(--yellow); }
  .address {
    position: absolute;
    right: 40px; top: 262px;
    text-align: right;
    font-size: 18px;
    line-height: 26px;
    letter-spacing: 0.04em;
  }
  .edge { position: absolute; left: 0; bottom: 0; width: 620px; height: 60px; }
</style>
</head>
<body>

<section class="card card-back">
  <div class="wordmark"><span class="mark-square"></span><span>Corbelle Group</span></div>
  <p class="offices">
    Sydney: (02) 7354 2260<span class="sep">|</span>Melbourne: (03) 9412 5063<br>
    Brisbane: (07) 3275 4190<span class="sep">|</span>Malaysia (JB): (+601) 8340 2967<br>
    Singapore: (+65) 9481 2736
  </p>
  <p class="services">Property Services<span class="sep">|</span>Financial Solutions<span class="sep">|</span>Special Projects.</p>
</section>

<section class="card card-front">
  <div class="wordmark"><span class="mark-square"></span><span>Corbelle Group</span></div>
  <div class="person">
    <h1 class="person-name">Derek Holm</h1>
    <p class="person-title">Project Manager</p>
  </div>
  <div class="divider"></div>
  <ul class="contacts">
    <li><svg viewBox="0 0 16 16"><path d="M4 1l3 3-2 2c1 2 3 4 5 5l2-2 3 3-2 3C7 15 1 9 1 3z" fill="none" stroke="var(--yellow)" stroke-width="1.6"/></svg><span>0428 613 954</span></li>
    <li><svg viewBox="0 0 16 16"><rect x="4" y="1" width="8" height="14" rx="1.5" fill="none" stroke="var(--yellow)" stroke-width="1.6"/><line x1="7" y1="12.5" x2="9" y2="12.5" stroke="var(--yellow)" stroke-width="1.4"/></svg><span>(02) 7354 2260</span></li>
    <li><svg viewBox="0 0 16 16"><rect x="1" y="3" width="14" height="10" fill="none" stroke="var(--yellow)" stroke-width="1.6"/><path d="M1 3l7 6 7-6" fill="none" stroke="var(--yellow)" stroke-width="1.4"/></svg><span>derek@corbellegroup.com</span></li>
    <li><svg viewBox="0 0 16 16"><circle cx="8" cy="8" r="6.5" fill="none" stroke="var(--yellow)" stroke-width="1.4"/><ellipse cx="8" cy="8" rx="3" ry="6.5" fill="none" stroke="var(--yellow)" stroke-width="1.2"/><line x1="1.5" y1="8" x2="14.5" y2="8" stroke="var(--yellow)" stroke-width="1.2"/></svg><span>www.<span class="highlight">corbellegroup</span>.com</span></li>
  </ul>
  <p class="address">Level 9, 42 Harlow Road W,<br>Parramatta NSW 2150</p>
  <svg class="edge" viewBox="0 0 620 60" preserveAspectRatio="none">
    <path d="M0 8 L270 24 Q285 25 292 28" fill="none" stroke="var(--white)" stroke-width="5"/>
    <path d="M0 42 L280 42 C310 42 320 30 350 30 L620 30 L620 60 L0 60 Z" fill="var(--yellow)"/>
  </svg>
</section>

</body>
</html>
```